we need a design for Water Bottle Lable Wrap
The product is called Corvane Water is a restructured water. its a very healthy and rejuvenating water
we were looking at using as a tag ling Restore, Recover, Rejuvenate.

```html
<!DOCTYPE html>
<html lang="en">
<head>
<meta charset="utf-8">
<title>Corvane Water – Label Wrap</title>
<link rel="stylesheet" href="https://fonts.googleapis.com/css2?family=Rubik:wght@400;500;600;800&display=swap">
<style>
  :root {
    --page-bg: #f4f5f6;
    --label-top: #ffffff;
    --label-mid: #8fd0c6;
    --label-base: #20a39a;
    --splash-soft: rgba(120, 190, 235, 0.55);
    --splash-fade: rgba(120, 190, 235, 0);
    --ink: #ffffff;
  }
  * { margin: 0; padding: 0; box-sizing: border-box; }
  html, body {
    width: 1200px;
    height: 1112px;
    overflow: hidden;
    background: var(--page-bg);
  }
  .canvas {
    position: relative;
    width: 1200px;
    height: 1112px;
  }
  .label-wrap {
    position: absolute;
    left: 132px;
    top: 54px;
    width: 936px;
    height: 1003px;
    overflow: hidden;
    background: linear-gradient(to bottom,
      var(--label-top) 0%,
      var(--label-top) 8%,
      var(--label-mid) 48%,
      var(--label-base) 66%,
      var(--label-base) 100%);
    box-shadow: 4px 6px 14px rgba(0, 0, 0, 0.18);
    font-family: "Rubik", sans-serif;
    color: var(--ink);
  }
  .splash-art {
    position: absolute;
    left: 0;
    top: 30px;
    width: 936px;
    height: 820px;
    background: radial-gradient(ellipse 60% 50% at 50% 50%,
      var(--splash-soft) 0%,
      var(--splash-fade) 100%);
  }
  .brand {
    position: absolute;
    left: 0;
    width: 100%;
    top: 340px;
    text-align: center;
  }
  .brand-name {
    font-weight: 800;
    font-size: 84px;
    line-height: 92px;
    letter-spacing: -1px;
    margin-left: 10px;
  }
  .brand-rule {
    width: 327px;
    height: 3px;
    background: var(--ink);
    margin: 14px auto 0 auto;
    position: relative;
    left: -3px;
  }
  .brand-type {
    font-weight: 600;
    font-size: 29px;
    line-height: 38px;
    letter-spacing: 0.5px;
    margin-top: 12px;
  }
  .tagline {
    position: absolute;
    left: 0;
    width: 100%;
    top: 836px;
    text-align: center;
    font-weight: 400;
    font-size: 33px;
    line-height: 46px;
    letter-spacing: 1px;
  }
  .tag-item { white-space: nowrap; margin: 0 4px; }
  .tick {
    display: inline-block;
    width: 24px;
    height: 22px;
    margin-right: 6px;
    vertical-align: -1px;
  }
</style>
</head>
<body>
<main class="canvas">
  <section class="label-wrap">
    <div class="splash-art" role="img" aria-label="Illustration of two flowing blue water splashes curving around the product name"></div>

    <div class="brand">
      <h1 class="brand-name">CORVANE<br>WATER</h1>
      <div class="brand-rule"></div>
      <p class="brand-type">RESTRUCTURED<br>WATER</p>
    </div>

    <p class="tagline">
      <span class="tag-item"><svg class="tick" viewBox="0 0 24 22"><path d="M2 12 L9 19 L22 3" fill="none" stroke="currentColor" stroke-width="3" stroke-linecap="round" stroke-linejoin="round"/></svg>RESTORE</span>
      <span class="tag-item"><svg class="tick" viewBox="0 0 24 22"><path d="M2 12 L9 19 L22 3" fill="none" stroke="currentColor" stroke-width="3" stroke-linecap="round" stroke-linejoin="round"/></svg>RECOVER</span><br>
      <span class="tag-item"><svg class="tick" viewBox="0 0 24 22"><path d="M2 12 L9 19 L22 3" fill="none" stroke="currentColor" stroke-width="3" stroke-linecap="round" stroke-linejoin="round"/></svg>REJUVENATE</span>
    </p>
  </section>
</main>
</body>
</html>
```